Glowmere Electrics website design

Electrical contractor in Perth that services the domestic and commercial markets. our services include but not limited to:

New Home Installations and Design
Commercial Shop Fit Outs
Rewires
Renovations
Switchboard Upgrades
Kitchen and Bathroom Renovations
RCD'S (Safety Switches)
Smoke Alarms
Power points
Security Lighting
Energy Efficient LED Lighting Designs
Garden Lighting
Downlights
General Electrical Maintenance
TV and Phone Points
Home Theatre Installs
Safety Certificates
24hr Call out service
Electric Hot Water Units
Credit cards accepted

www.facebook.com/glowmereelectrics

Industry/Entity Type

Contractor

Number of Pages Required

5+ page

Font styles to use
Sans Serif

Colors
acd037
fbee3e

Requirements
Must have
• contact page, services page, about us, careers page, somewhere I can put some testimonials, somewhere potential clients can book our services online, on the homepage somewhere showing that we can provide 24/7 emergency service
Nice to have
• icon stating that we accept all major credit cards

```html
<!DOCTYPE html>
<html lang="en">
<head>
<meta charset="utf-8">
<title>Glowmere Electrics</title>
<link rel="stylesheet" href="https://fonts.googleapis.com/css2?family=Questrial&family=Mulish:wght@400;600;700&display=swap">
<style>
:root{
  --blue:#0b4a82;
  --yellow:#e4e03a;
  --lime:#acd037;
  --gold:#f0d43a;
  --text:#333;
  --field:#f4f4f4;
  --band:#ededed;
  --footer:#262626;
}
*{box-sizing:border-box;margin:0;padding:0}
html,body{width:1200px;height:1200px;overflow:hidden;background:#fff}
body{position:relative;font-family:"Mulish",sans-serif;color:var(--text)}
.head{position:absolute;left:0;top:0;width:1200px;height:160px}
.brand{position:absolute;left:173px;top:40px;display:flex;align-items:center;gap:14px}
.brand-dot{width:40px;height:40px;border-radius:50%;background:var(--blue)}
.brand-name{font-family:"Questrial",sans-serif;font-size:34px;color:var(--blue);line-height:1}
.reg{position:absolute;left:410px;top:118px;font-size:8px;color:var(--blue);line-height:10px}
.toplinks{position:absolute;right:172px;top:30px;font-size:14px;color:#333;display:flex;gap:12px;align-items:center;letter-spacing:-.3px}
.toplinks .cards{color:var(--lime);display:flex;align-items:center;gap:6px}
.contactrow{position:absolute;right:172px;top:66px;display:flex;gap:28px;align-items:center}
.booking{color:var(--gold);font-weight:700;font-size:13px;display:flex;gap:6px;align-items:center;letter-spacing:-.3px}
.phone{color:var(--blue);font-weight:700;font-size:15px;display:flex;gap:6px;align-items:center;letter-spacing:-.3px}
.nav{position:absolute;right:172px;top:102px;display:flex;gap:15px;font-size:16px;color:#222;letter-spacing:-.4px}
.nav .active{color:var(--blue);font-weight:700;border-bottom:2px solid var(--blue);padding-bottom:4px}
.hero{position:absolute;left:0;top:160px;width:1200px;height:437px;overflow:hidden}
.hero-photo{position:absolute;inset:0;background:linear-gradient(90deg,#e9e4e2 0%,#d8cfcc 35%,#c9c4c2 55%,#e8e8ea 75%,#cfd4dd 100%)}
.hero-worker{position:absolute;left:760px;top:10px;width:240px;height:427px;border-radius:110px 110px 0 0;background:linear-gradient(180deg,#d9c2ad 0%,#3b5fb8 30%,#2a4ea6 100%);opacity:.9}
.hero-title{position:absolute;left:170px;top:158px;font-family:"Questrial",sans-serif;font-weight:400;font-size:43px;color:var(--blue);letter-spacing:-.5px}
.hero-copy{position:absolute;left:173px;top:221px;width:558px;font-family:"Questrial",sans-serif;font-size:16px;line-height:19px;color:#222}
.badge{position:absolute;left:173px;top:354px;width:190px;height:52px;border-radius:6px;background:#263a55;opacity:.85}
.arrow{position:absolute;top:191px;width:50px;height:50px;border-radius:50%;background:rgba(255,255,255,.55);display:flex;align-items:center;justify-content:center}
.welcome{position:absolute;left:172px;top:641px;width:560px}
.welcome small{font-family:"Questrial",sans-serif;font-size:14px;color:#333;display:block}
.welcome h1{font-family:"Questrial",sans-serif;font-weight:400;font-size:33px;color:var(--blue);line-height:34px;margin-bottom:16px}
.welcome h1 span{color:var(--yellow)}
.welcome p{font-size:12.3px;line-height:15px;color:#333;margin-bottom:9px}
.feature{position:absolute;top:822px;width:274px;height:90px;background:#f7f7f7;display:flex;align-items:center}
.feature .ico{width:128px;display:flex;justify-content:center}
.feature .label{border-left:1px solid var(--blue);padding-left:10px;font-family:"Questrial",sans-serif;font-size:16px;line-height:19px;color:var(--blue)}
.book{position:absolute;left:757px;top:640px;width:271px}
.book h2{font-family:"Questrial",sans-serif;font-weight:400;font-size:22px;line-height:25px;color:var(--blue);margin-bottom:12px}
.field{background:var(--field);height:40px;margin-bottom:4px;padding:12px 18px;font-size:15px;color:#444}
.field b{color:#d22;font-weight:400}
.field.msg{height:74px;margin-bottom:8px}
.send{height:40px;background:var(--blue);color:#fff;font-weight:700;font-size:21px;text-align:center;line-height:40px;letter-spacing:.5px}
.services{position:absolute;left:0;top:965px;width:1200px;height:172px;background:var(--band)}
.services h2{position:absolute;left:172px;top:34px;font-family:"Questrial",sans-serif;font-weight:400;font-size:22px;color:var(--blue)}
.svc-cols{position:absolute;left:172px;top:68px;display:flex}
.svc-cols ul{list-style:none;width:219px;font-size:10.4px;font-weight:700;line-height:12.3px;color:#777}
.svc-cols li::before{content:"✓ ";color:#777}
.svc-cols li.on{color:var(--blue)}
.svc-cols li.on::before{color:var(--blue)}
.foot{position:absolute;left:0;top:1137px;width:1200px;height:63px;background:var(--footer)}
.copy{position:absolute;left:173px;top:25px;font-size:10px;font-weight:700;color:var(--yellow);letter-spacing:-.2px}
.foot-nav{position:absolute;right:174px;top:25px;display:flex;gap:10px;font-size:10px;color:#ddd;letter-spacing:-.2px}
.foot-nav .active{color:var(--yellow);font-weight:700}
</style>
</head>
<body>
<header class="head">
  <div class="brand"><span class="brand-dot"></span><span class="brand-name">Glowmere Electrics</span></div>
  <div class="reg">EC 10428<br>ABN 12345678901</div>
  <div class="toplinks">
    <span>Login</span><span>|</span><span>Register</span><span>|</span>
    <span class="cards"><svg width="22" height="16" viewBox="0 0 22 16"><rect x="1" y="3" width="16" height="10" rx="2" fill="none" stroke="#0b4a82" stroke-width="1.6"/><path d="M9 9l4 4 8-11" fill="none" stroke="#acd037" stroke-width="2"/></svg>We accepts all major credit cards</span>
  </div>
  <div class="contactrow">
    <span class="booking"><svg width="20" height="20" viewBox="0 0 20 20"><rect x="1" y="3" width="18" height="16" rx="2" fill="none" stroke="#f0d43a" stroke-width="1.6"/><line x1="1" y1="8" x2="19" y2="8" stroke="#f0d43a" stroke-width="1.6"/><text x="10" y="17" font-size="8" text-anchor="middle" fill="#f0d43a" font-family="sans-serif">7</text></svg>MAKE YOUR BOOKING</span>
    <span class="phone"><svg width="24" height="24" viewBox="0 0 24 24"><circle cx="12" cy="12" r="10" fill="none" stroke="#0b4a82" stroke-width="1.6"/><text x="12" y="14" font-size="7" text-anchor="middle" fill="#0b4a82" font-family="sans-serif">24h</text></svg>10 20 30 40 50</span>
  </div>
  <nav class="nav"><span class="active">Home</span><span>Services</span><span>About Us</span><span>Careers</span><span>Testimonials</span><span>&nbsp;Contact</span></nav>
</header>

<section class="hero">
  <div class="hero-photo" role="img" aria-label="Close-up photo of hands wiring a power outlet"></div>
  <div class="hero-worker" role="img" aria-label="Electrician in blue overalls carrying a coil of cable"></div>
  <h2 class="hero-title">GLOWMERE ELECTRICS</h2>
  <p class="hero-copy">Duis autem vel eum iriure dolor in hendrerit in vulputate velit esse molestie consequat, vel illum dolore eu feugiat nulla facilisis at vero eros et accumsan et iusto odio dignissim qui blandit praesent luptatum zzril delenit augue duis dolore te feugait nulla facilisi.</p>
  <div class="badge" role="img" aria-label="Trade association member badge"></div>
  <div class="arrow" style="left:65px"><svg width="14" height="24" viewBox="0 0 14 24"><path d="M12 2L2 12l10 10" fill="none" stroke="#333" stroke-width="1.6"/></svg></div>
  <div class="arrow" style="left:1087px"><svg width="14" height="24" viewBox="0 0 14 24"><path d="M2 2l10 10L2 22" fill="none" stroke="#333" stroke-width="1.6"/></svg></div>
</section>

<section class="welcome">
  <small>WELCOME</small>
  <h1><span>GLOWMERE</span> ELECTRICS</h1>
  <p>Lorem ipsum dolor sit amet, consectetuer adipiscing elit, sed diam nonummy nibh euismod tincidunt ut laoreet dolore magna aliquam erat volutpat. Ut wisi enim ad minim veniam, quis nostrud exerci tation ullamcorper suscipit lobortis nisl ut aliquip ex ea commodo consequat.</p>
  <p>Duis autem vel eum iriure dolor in hendrerit in vulputate velit esse molestie consequat, vel illum dolore eu feugiat nulla facilisis at vero eros et accumsan et iusto odio dignissim qui blandit praesent luptatum zzril delenit augue duis dolore te feugait nulla facilisi.</p>
</section>

<div class="feature" style="left:172px">
  <div class="ico"><svg width="74" height="64" viewBox="0 0 74 64"><path d="M14 44A26 26 0 1 1 46 58" fill="none" stroke="#0b4a82" stroke-width="4"/><path d="M8 38l6 8 7-7" fill="none" stroke="#0b4a82" stroke-width="4"/><text x="37" y="36" font-size="18" font-weight="700" text-anchor="middle" fill="#0b4a82" font-family="sans-serif">24/7</text><text x="37" y="48" font-size="9" text-anchor="middle" fill="#0b4a82" font-family="sans-serif">365</text></svg></div>
  <div class="label">24/7<br>EMERGENCY<br>SERVICE</div>
</div>
<div class="feature" style="left:456px">
  <div class="ico"><svg width="76" height="56" viewBox="0 0 76 56"><g transform="rotate(30 30 30)"><rect x="8" y="14" width="44" height="28" rx="3" fill="#fff" stroke="#0b4a82" stroke-width="4"/><line x1="8" y1="24" x2="52" y2="24" stroke="#0b4a82" stroke-width="5"/></g><path d="M40 34l10 12 22-40" fill="none" stroke="#e4e03a" stroke-width="7"/></svg></div>
  <div class="label">WE ACCEPT<br>ALL MAJOR<br>CREDIT CARDS</div>
</div>

<aside class="book">
  <h2>BOOK YOUR<br>APPOINTMENT NOW!</h2>
  <div class="field">Name<b>*</b></div>
  <div class="field">E-mail<b>*</b></div>
  <div class="field msg">Message</div>
  <div class="send">SEND</div>
</aside>

<section class="services">
  <h2>OUR SERVICES</h2>
  <div class="svc-cols">
    <ul><li class="on">New Home Installations and Design</li><li>Commercial Shop Fit Outs</li><li>Rewires</li><li>Renovations</li><li>Switchboard Upgrades</li></ul>
    <ul><li>Kitchen and Bathroom Renovations</li><li>RCD'S (Safety Switches)</li><li>Smoke Alarms</li><li>Power points</li><li>Security Lighting</li></ul>
    <ul><li>Energy Efficient LED Lighting Designs</li><li>Garden Lighting</li><li>Downlights</li><li>General Electrical Maintenance</li><li>TV and Phone Points</li></ul>
    <ul><li>Home Theatre Installs</li><li>Safety Certificates</li><li>24hr Call out service</li><li>Electric Hot Water Units</li><li>ETC</li></ul>
  </div>
</section>

<footer class="foot">
  <div class="copy">©2014 Glowmere Electric . Inc All Rights Reserved.</div>
  <nav class="foot-nav"><span class="active">Home</span><span>Services</span><span>About Us</span><span>Careers</span><span>Testimonials</span><span>Contact</span></nav>
</footer>
</body>
</html>
```